QDL Kids Choir

Card to hand out or mail out with our own mailing labels. Needs to be appealing to families with children ages 4 yrs through 6th grade, who have an interest in musical experiences for the kids in a contemporary Bible teaching/church setting. We have 3 different kids choirs: 4-yr-old & Kindergarten Choir, 1st-3rd grade choir, and 4th-6th grade choir. This is a FREE after-school program every Tuesday from 3:30-5:00. Transportation for grades 1-6 from local schools is provided. Parents should expect their children to experience fun, friends, music, recreation, games, snacks, character building, Bible teaching, in an encouraging church environment.

Church

• Bight colors

```html
<!DOCTYPE html>
<html lang="en">
<head>
<meta charset="utf-8">
<title>QDL Kids Choir – Free After-School Program</title>
<link rel="stylesheet" href="https://fonts.googleapis.com/css2?family=Arimo:wght@700&display=swap">
<style>
  :root{
    --sun:#f8d71b;
    --amber:#f39b1c;
    --sky:#2aa3dc;
    --ocean:#1a7fc4;
    --deep:#0f5fa5;
    --berry:#8e1a1f;
    --red:#c8202a;
    --green:#2e9b3a;
    --blue:#1f6fc0;
    --navy:#1f2f6b;
    --white:#ffffff;
  }
  *{margin:0;padding:0;box-sizing:border-box}
  html,body{width:1200px;height:930px;overflow:hidden;background:var(--white)}
  body{font-family:"Arimo",Arial,sans-serif;font-weight:700}
  .card{position:relative;width:1200px;height:930px;overflow:hidden}
  .backdrop{position:absolute;inset:0}
  .ministry-badge{
    position:absolute;left:68px;top:376px;width:224px;height:224px;border-radius:50%;
    background:var(--white);border:4px solid #d8d8d8;
    display:flex;flex-direction:column;align-items:center;justify-content:center;
    color:var(--berry);text-align:center;line-height:1.15;
  }
  .ministry-badge .title{font-size:25px}
  .ministry-badge .church{font-size:15px;margin-top:10px}
  .ministry-badge .town{font-size:12px;margin-top:3px}
  .free-seal{
    position:absolute;left:333px;top:408px;width:144px;height:144px;border-radius:50%;
    background:radial-gradient(circle at 40% 35%,#e0353d,var(--red) 60%,#9d141b);
    border:3px solid var(--white);
    display:flex;flex-direction:column;align-items:center;justify-content:center;
    color:var(--white);text-align:center;line-height:1.05;
  }
  .free-seal .free{font-size:33px}
  .free-seal .what{font-size:19px}
  .choirs-heading{
    position:absolute;left:177px;top:642px;width:660px;height:63px;border-radius:12px;
    background:linear-gradient(#ffffff,#e9e9e9);
    box-shadow:0 3px 6px rgba(0,0,0,.35);
    color:var(--berry);font-size:48px;
    display:flex;align-items:center;justify-content:center;
  }
  .choir-list{position:absolute;left:105px;top:720px;display:flex;gap:12px}
  .choir{
    width:270px;height:162px;border-radius:14px;border:3px solid rgba(255,255,255,.75);
    display:flex;align-items:center;justify-content:center;text-align:center;
    color:var(--white);font-size:33px;line-height:1.2;
    text-shadow:1px 2px 2px rgba(0,0,0,.45);
    box-shadow:0 3px 6px rgba(0,0,0,.3);
  }
  .choir--little{background:linear-gradient(#3fb54a,var(--green))}
  .choir--primary{background:linear-gradient(#3189d6,var(--blue))}
  .choir--upper{background:linear-gradient(#d8333b,var(--red));width:273px}
  .church-name{
    position:absolute;left:955px;top:708px;width:225px;
    color:var(--navy);font-size:29px;line-height:1.2;text-align:center;letter-spacing:1px;
  }
</style>
</head>
<body>
<main class="card">
  <svg class="backdrop" width="1200" height="930" viewBox="0 0 1200 930">
    <defs>
      <linearGradient id="sunGlow" x1="0" y1="0" x2="1" y2="0.4">
        <stop offset="0" stop-color="var(--sun)"/>
        <stop offset="0.6" stop-color="#f6c31a"/>
        <stop offset="1" stop-color="var(--amber)"/>
      </linearGradient>
      <linearGradient id="photoTone" x1="0" y1="0" x2="1" y2="1">
        <stop offset="0" stop-color="#8a6a4c"/>
        <stop offset="0.45" stop-color="#d9d3c9"/>
        <stop offset="0.8" stop-color="#a88462"/>
        <stop offset="1" stop-color="#5a3f2b"/>
      </linearGradient>
    </defs>
    <rect width="1200" height="930" fill="url(#sunGlow)"/>
    <polygon points="0,28 600,0 1200,0 1200,450 0,410" fill="url(#photoTone)" role="img" aria-label="Photo of a children's choir in white robes singing from sheet music in a church"/>
    <polygon points="600,0 1200,0 1200,75 880,38" fill="var(--ocean)"/>
    <polygon points="0,410 1200,450 1200,620 0,560" fill="var(--ocean)"/>
    <polygon points="0,490 1200,545 1200,620 0,580" fill="var(--sky)"/>
    <polygon points="980,450 1200,450 1200,650" fill="var(--deep)"/>
    <polygon points="0,582 1200,622 1200,640 0,600" fill="#fff6b0" opacity=".6"/>
    <polygon points="0,640 90,700 60,930 0,930" fill="var(--sky)"/>
  </svg>

  <div class="ministry-badge">
    <span class="title">Kids Ministry</span>
    <span class="church">Grace Hill Church</span>
    <span class="town">Maple Ridge, Kansas</span>
  </div>

  <div class="free-seal">
    <span class="free">FREE</span>
    <span class="what">after-school<br>program</span>
  </div>

  <h1 class="choirs-heading">3 different kids choirs</h1>

  <div class="choir-list">
    <div class="choir choir--little">4-yr-old &amp;<br>Kindergarten<br>Choir</div>
    <div class="choir choir--primary">1st-3rd grade<br>choir</div>
    <div class="choir choir--upper">4th-6th grade<br>choir</div>
  </div>

  <div class="church-name">GRACE HILL<br>CHURCH</div>
</main>
</body>
</html>
```